Banner Ad Design Project

We have a Website

We need a better Banner for better marketing what we do which is Crowd Funding
We need the banner to be bright Colourful and to paint a picture

We have prepared a very good Breif for you, we will provide prompt feedback

Thankyou Darren

Project Deadline Extended
Reason: Quality takes time We have several projects and are looking for an ongoing supplier.

Target Market(s)

21 to 65 with some money and online, look at fundspryte, or pledgeorbit.com

Industry/Entity Type

Marketing

Requirements
Must have
• Bright Colors and Bold
Nice to have
• Jumps out at you, Positive Vibrant
Should not have
• Not Dull

```html
<!DOCTYPE html>
<html lang="en">
<head>
<meta charset="utf-8">
<title>Beckon – Crowd Funding</title>
<link href="https://fonts.googleapis.com/css2?family=Varela+Round&family=Cabin:wght@400;500;600&family=Cormorant+Garamond:wght@500&family=Josefin+Sans:wght@300;400&family=Oswald:wght@300;400&family=Arimo:wght@400;700&display=swap" rel="stylesheet">
<style>
:root{
  --ink:#555;
  --navy:#1e3f66;
  --band:#1d5080;
  --banner-green:#5ec65b;
  --banner-dark:#3fa83d;
  --btn-green:#6cc43a;
  --btn-green-dark:#4ea524;
  --footer:#2b5e8e;
  --footer-strip:#4a77a2;
  --box-blue:#3d74a8;
  --link-blue:#3b5998;
  --green-title:#1e6b4f;
  --blue-title:#1e3f80;
  --orange-title:#f5a623;
  --coral:#f07050;
  --rose:#d03060;
  --white:#fff;
}
*{box-sizing:border-box;margin:0;padding:0}
html,body{width:1197px;height:1200px;overflow:hidden;background:var(--white)}
body{position:relative;font-family:"Arimo",Arial,sans-serif;color:var(--ink)}
.abs{position:absolute}

.header{left:0;top:0;width:1197px;height:188px;background:linear-gradient(#fff 0,#fff 125px,#e6e6e6 188px)}
.brand{left:130px;top:8px;display:flex;align-items:center;gap:12px}
.brand-mark{width:58px;height:58px;border-radius:50%;background:#2f9ad6}
.brand-name{font-family:"Varela Round",sans-serif;font-size:40px;color:#7a7a7a;font-weight:400}
.account{left:862px;top:53px;display:flex;align-items:center;gap:6px;font-size:11px;font-weight:700;color:#333}
.login{width:66px;height:21px;background:var(--link-blue);color:#fff;font-size:11px;font-weight:700;display:flex;align-items:center;justify-content:flex-end;padding-right:8px;border:1px solid #29487d}
.social-sq{width:20px;height:20px;background:#4fb6e8;border-radius:3px}

.nav{left:142px;top:87px;width:915px;height:40px;background:#fff;border:1px solid #ddd;box-shadow:0 2px 4px rgba(0,0,0,.12)}
.nav-links{left:17px;top:12px;display:flex;font-size:12px;color:#555}
.nav-links span{padding:0 8px}
.nav-links span:first-child{padding-left:0}
.nav-links .sep{color:#f0a030;padding:0 4px}
.search-input{left:657px;top:6px;width:188px;height:26px;border:1px solid #ccc;font-size:11px;color:#999;padding:6px 7px}
.search-btn{left:845px;top:6px;width:62px;height:26px;background:var(--btn-green);color:#fff;font-size:12px;display:flex;align-items:center;justify-content:center}
.browse{left:807px;top:145px;width:248px;height:36px;background:linear-gradient(#8ad64e,var(--btn-green-dark));border:1px solid #4a9a22;color:#fff;font-weight:700;font-size:14px;display:flex;align-items:center;justify-content:center;letter-spacing:.3px}

.band{left:0;top:188px;width:1197px;height:122px;background:var(--band)}
.hero{left:97px;top:188px;width:1000px;height:122px;background:var(--banner-green);overflow:hidden}
.hero-wave{left:0;top:0}
.hero-kicker{left:33px;top:16px;font-family:"Josefin Sans",sans-serif;font-size:31px;color:#fff;font-weight:400}
.hero-title{left:33px;top:38px;font-family:"Cormorant Garamond",serif;font-size:72px;color:#fff;letter-spacing:-1px;line-height:1}
.hero-offer{right:12px;top:30px;text-align:right;font-family:"Josefin Sans",sans-serif;font-weight:300;color:#fff;line-height:1}
.hero-offer .big{font-size:27px}
.hero-offer .small{font-size:21px;margin-top:2px}

.section-title{left:130px;top:330px;font-size:17px;font-weight:700;color:var(--navy);letter-spacing:.3px}
.divider{top:384px;height:452px;border-left:1px dashed #bbb}
.feature{top:394px;width:360px;text-align:center}
.feature h2{font-family:"Cabin",sans-serif;font-weight:500;font-size:24px;line-height:26px}
.feature .art{margin:34px auto 0;border-radius:8px}
.feature .cta{position:absolute;left:0;width:100%;top:414px;font-family:"Oswald",sans-serif;font-weight:300;font-size:20px;letter-spacing:.3px}

.footer{left:0;top:871px;width:1197px;height:278px;background:var(--footer)}
.footer-strip{left:0;top:1149px;width:1197px;height:51px;background:var(--footer-strip)}
.foot-head{font-size:12px;font-weight:700;color:#fff}
.foot-list{font-size:11px;color:#fff;line-height:18px;list-style:none}
.connect-icons{left:400px;top:941px;display:flex;gap:15px}
.connect-icons span{width:33px;height:33px;border-radius:6px}
.newsletter{left:363px;top:989px;width:251px;height:81px;background:var(--box-blue);border-radius:6px;border:1px solid #5b8cbb}
.newsletter h3{position:absolute;left:12px;top:8px;font-family:"Cabin",sans-serif;font-weight:400;font-size:16px;color:#fff}
.news-input{left:9px;top:35px;width:167px;height:30px;background:#fff;font-size:11px;color:#333;padding:9px 4px}
.news-btn{left:186px;top:37px;width:55px;height:27px;border-radius:4px;background:linear-gradient(#fff,#cfd9e4);color:var(--box-blue);font-family:"Cabin",sans-serif;font-weight:600;font-size:15px;display:flex;align-items:center;justify-content:center}

.fan-box{left:768px;top:882px;width:292px;height:257px;background:#fff;border:1px solid #bbb}
.fan-logo{left:10px;top:8px;width:48px;height:48px;background:#e8eef5}
.fan-name{left:65px;top:10px;font-size:13px;font-weight:700;color:var(--link-blue)}
.fan-like{left:66px;top:33px;width:51px;height:21px;border:1px solid #ccd;background:#f2f2f2;font-size:11px;color:var(--link-blue);display:flex;align-items:center;gap:4px;padding-left:5px}
.fan-like i{width:11px;height:11px;background:var(--link-blue)}
.fan-rule{left:10px;width:275px;border-top:1px solid #ddd}
.fan-count{left:10px;top:75px;font-size:11px;color:#333}
.fan-count b{font-weight:400;color:var(--link-blue)}
.fan-grid{left:10px;top:98px;width:263px;height:104px;background:linear-gradient(90deg,#b9a799,#c8d0dc,#6f6f6f,#a79a8c,#c8d0dc);}
.fan-foot{left:11px;top:218px;font-size:11px;color:#555;display:flex;gap:6px;align-items:center}
.fan-foot i{width:11px;height:11px;background:var(--link-blue)}

.copyright{left:130px;top:1170px;font-size:11px;color:#fff}
.pay-badge{left:366px;top:1159px;width:53px;height:34px;background:#eef1f5;border-radius:3px}
.bottom-links{right:152px;top:1169px;display:flex;font-size:11px;color:#fff}
.bottom-links span{padding:0 5px}
.bottom-links .sep{padding:0}
</style>
</head>
<body>

<header class="header abs">
  <div class="brand abs"><span class="brand-mark"></span><span class="brand-name">Beckon</span></div>
  <div class="account abs"><span class="login">Log In</span><span class="social-sq"></span><span>SIGN IN | SIGN UP</span></div>
  <nav class="nav abs">
    <div class="nav-links abs">
      <span>Home</span><span class="sep">|</span><span>Search</span><span class="sep">|</span><span>Create</span><span class="sep">|</span><span>Learn More</span><span class="sep">|</span><span>About Us</span><span class="sep">|</span><span>Tips &amp; Tricks</span><span class="sep">|</span>
    </div>
    <div class="search-input abs">please enter search keyword</div>
    <div class="search-btn abs">Search</div>
  </nav>
  <div class="browse abs">BROWSE ALL PROJECTS</div>
</header>

<section class="band abs"></section>
<section class="hero abs">
  <svg class="hero-wave abs" width="1000" height="14" viewBox="0 0 1000 14">
    <path d="M0 0H1000V8Q990 14 980 8T960 8T940 8T920 8T900 8T880 8T860 8T840 8T820 8T800 8T780 8T760 8T740 8T720 8T700 8T680 8T660 8T640 8T620 8T600 8T580 8T560 8T540 8T520 8T500 8T480 8T460 8T440 8T420 8T400 8T380 8T360 8T340 8T320 8T300 8T280 8T260 8T240 8T220 8T200 8T180 8T160 8T140 8T120 8T100 8T80 8T60 8T40 8T20 8T0 8Z" fill="#3fa83d"/>
  </svg>
  <div class="hero-kicker abs">The Noble Way To</div>
  <div class="hero-title abs">Back &amp; Trail Ingenuity</div>
  <div class="hero-offer abs">
    <div class="big">0% Commission</div>
    <div class="small">Keep 100% of the money you raise</div>
    <div class="small">*Limited time offer</div>
  </div>
</section>

<h1 class="section-title abs">FEATURED PROJECTS</h1>
<div class="divider abs" style="left:419px"></div>
<div class="divider abs" style="left:792px"></div>

<article class="feature abs" style="left:78px">
  <h2 style="color:var(--green-title)">Personal Donation<br>Campaign</h2>
  <div class="art" role="img" aria-label="Illustration of a pink piggy bank with a gold coin, a cheque book and a pen" style="width:270px;height:280px;background:radial-gradient(circle at 60% 60%,#f7a890,#f5d9a0 55%,#fff 75%)"></div>
  <div class="cta" style="color:var(--coral)">PAY IT FORWARD</div>
</article>

<article class="feature abs" style="left:419px">
  <h2 style="color:var(--blue-title)">Projects, Products<br>&amp; Startups</h2>
  <div class="art" role="img" aria-label="Illustration of a hammer, a glowing light bulb, a desktop computer and scissors" style="width:310px;height:290px;background:radial-gradient(circle at 50% 55%,#b7cfe4,#e9e3b0 50%,#fff 75%)"></div>
  <div class="cta" style="color:var(--blue-title)">FUND YOUR PROJECT</div>
</article>

<article class="feature abs" style="left:778px">
  <h2 style="color:var(--orange-title)">Raise Money For<br>Your Chosen Charity</h2>
  <div class="art" role="img" aria-label="Illustration of a large pink awareness ribbon between a puzzle ribbon and an orange ribbon" style="width:240px;height:280px;background:radial-gradient(circle at 50% 45%,#f0a0c0,#f7d6e4 55%,#fff 75%)"></div>
  <div class="cta" style="color:var(--rose)">GIVE HOPE</div>
</article>

<footer class="footer abs">
  <div class="foot-head abs" style="left:130px;top:28px">DISCOVER GREAT PROJECTS</div>
  <ul class="foot-list abs" style="left:129px;top:54px"><li>Art</li><li>Comics</li><li>Dance</li><li>Design</li><li>Fashion</li><li>Film &amp; Video</li><li>Food</li><li>Games</li><li>Music</li><li>Photography</li></ul>
  <ul class="foot-list abs" style="left:216px;top:54px"><li>Technology</li><li>Theatre</li><li>Writing &amp; Publishing</li></ul>
  <div class="foot-head abs" style="left:400px;top:25px;font-size:13px">CONNECT WITH BECKON</div>
</footer>
<div class="connect-icons abs"><span style="background:#4fb6e8"></span><span style="background:#3b6aa8"></span><span style="background:#f08a24"></span></div>
<div class="newsletter abs">
  <h3>Subscribe for Newsletter</h3>
  <div class="news-input abs">Enter email</div>
  <div class="news-btn abs">Join</div>
</div>

<aside class="fan-box abs">
  <div class="fan-logo abs"></div>
  <div class="fan-name abs">Beckon</div>
  <div class="fan-like abs"><i></i>Like</div>
  <div class="fan-rule abs" style="top:68px"></div>
  <div class="fan-count abs">2,463 people like <b>Beckon</b>.</div>
  <div class="fan-grid abs" role="img" aria-label="Grid of ten small member profile photos"></div>
  <div class="fan-rule abs" style="top:211px"></div>
  <div class="fan-foot abs"><i></i>Linkbook social plugin</div>
</aside>

<div class="footer-strip abs"></div>
<div class="copyright abs">Beckon Copyright © 2011 All Rights Reserved.</div>
<div class="pay-badge abs"></div>
<div class="bottom-links abs"><span>Create</span><span class="sep">|</span><span>Terms And Conditions</span><span class="sep">|</span><span>Privacy Policy</span><span class="sep">|</span><span>Contact Us</span><span class="sep">|</span><span>Learn More</span><span class="sep">|</span><span>About Us</span><span class="sep">|</span></div>

</body>
</html>
```